BrimstoneHoldingsLLC

Real Estate Investment. Buy/Sell house/investment . Trustworthy,Reliable, and friendly

Industry/Entity Type

Real Estate

Contact Information for Business Card

BrimstoneHoldings@mailtrove.com
555-413-2960
Tamsin-Leigh Okafor

```html
<!DOCTYPE html>
<html lang="en">
<head>
<meta charset="UTF-8">
<title>Brimstone Holdings LLC — Business Card</title>
<link rel="stylesheet" href="https://fonts.googleapis.com/css2?family=Arimo:wght@400;700&family=Tinos&display=swap">
<style>
  :root {
    --card-green: #5bbd98;
    --ink: #000000;
  }
  html, body {
    margin: 0;
    padding: 0;
    width: 1200px;
    height: 702px;
    overflow: hidden;
    background: var(--card-green);
  }
  .card {
    position: relative;
    width: 1200px;
    height: 702px;
    background: var(--card-green);
    color: var(--ink);
    overflow: hidden;
  }
  .holder-name {
    position: absolute;
    left: 74px;
    top: 38px;
    margin: 0;
    font-family: "Arimo", Arial, sans-serif;
    font-weight: 700;
    font-size: 48px;
    letter-spacing: 1px;
    word-spacing: 8px;
    line-height: 1;
  }
  .company-name {
    position: absolute;
    left: 603px;
    top: 345px;
    margin: 0;
    transform: translate(-50%, -50%) rotate(-11.3deg);
    white-space: nowrap;
    font-family: "Arimo", Arial, sans-serif;
    font-weight: 400;
    font-size: 82px;
    letter-spacing: 3px;
    word-spacing: 10px;
    line-height: 1;
  }
  .contact-email {
    position: absolute;
    left: 46px;
    top: 604px;
    font-family: "Arimo", Arial, sans-serif;
    font-weight: 700;
    font-size: 40px;
    line-height: 1;
  }
  .contact-phone {
    position: absolute;
    right: 42px;
    top: 600px;
    font-family: "Tinos", "Times New Roman", serif;
    font-weight: 400;
    font-size: 48px;
    line-height: 1;
  }
</style>
</head>
<body>
  <main class="card">
    <h1 class="holder-name">Tamsin-Leigh Okafor</h1>
    <p class="company-name">Brimstone Holdings LLC</p>
    <span class="contact-email">BrimstoneHoldings@mailtrove.com</span>
    <span class="contact-phone">555-413-2960</span>
  </main>
</body>
</html>
```